Design Brief: Premium Supplement Packaging for Velo Slate
Client: Kep BrightMeals
Product: Velo Slate – Advanced Supplement for Fat and Carb Blocking
Label Dimensions: 5.829 in (W) x 2.381 in (H)
Bottle Size: 1.9 in diameter x 3.6 in height (round bottle)
Bottle Color: Dark transparent green

Project Background
We are Kep BrightMeals, a premium health and wellness brand committed to innovation in food science. Our patented natural inhibitor technology helps people eat smarter without sacrificing taste or lifestyle.

Velo Slate is one of our hero products. It’s a dietary supplement designed to block fat, burn body fat, and inhibit carbs and sugars from meals—ideal for customers who are focused on weight management, ketogenic eating, or healthy living.

We are redesigning our current packaging to better align with our premium, science-forward brand image. The design submitted previously (attached) was not accepted due to its dated aesthetics, overuse of gradients, and lack of modern polish.

What We’re Looking For
Modern, minimal, and clean aesthetic
Must reflect premium quality and scientific credibility
Clean typography with visual hierarchy
Smart use of white/negative space
A design that pops against the dark transparent green bottle
Avoid heavy gradients or oversaturated colors

Elegant layout for supplement facts and usage instructions
Design should communicate the benefit and function clearly
6 different design options requested

Inspirational Style Examples
Cadence vitamins
Fern probiotics
Harbor Sprouts
Nevi or Tallow packaging
More inspiration:
https://www.moodlane.example/pin/210050770115922375/
https://www.moodlane.example/pin/851813717045134467/
https://www.moodlane.example/pin/502503270943410882/
https://www.moodlane.example/pin/22940279347217776/

Packaging Copy
Front Panel (Primary Panel)
Kep BrightMeals™
VeloSlate™
Advanced Fat + Carb Inhibitor
Block up to 10g of Fat & 85% of Carbs per serving
Burn more stored body fat naturally
60 Capsules | Dietary Supplement | 775mg per capsule

Side Panel 1 (Suggested Use & Warning)
Suggested Use:
Take with water 25 minutes before a high-carb or high-fat meal.
Refer to dosage chart: Fat(g) ÷ 6 = Number of capsules

Warning:
For adults only. Consult a healthcare provider if you are pregnant, nursing, on medication, or have a medical condition.

Storage: Store at 55–75°F. Protect from moisture and heat.

Side Panel 2 (Supplement Facts)
[Maintain layout but modernize font/box style—content remains the same]
Polysaccharide – 1325 mg
Cissus Asthisonhara Dicotyledon – 150 mg
Irvingia Gabonensis – 75 mg
Other ingredients: Magnesium sulfate, 100% vegetable-based capsules. Free of: Milk, eggs, peanuts, tree nuts, shellfish, fish, soy, gluten, titanium dioxide.

Manufactured in the USA (use attached flag) for Kep BrightMeals (use logo)
KepNourish.example

Design Deliverables
Front and back label concepts
Fonts and color hex values used
Mockup of label on a dark green bottle
Rendered 3D mockup

Attached you will find our tortilla chips design, the barcode, packaging bottle, branding guide, and logos. You will also notice two versions of the Velo Slate packaging: the white label is the current version that we want to update, and the green label is the proposed design we received, which does not meet our standards.

```html
<!DOCTYPE html>
<html lang="en">
<head>
<meta charset="utf-8">
<title>Velo Slate – Side &amp; Front Label</title>
<link href="https://fonts.googleapis.com/css2?family=Poppins:wght@300;400;500&family=Barlow+Condensed:wght@400;500;600;700&family=Oswald:wght@300;700&display=swap" rel="stylesheet">
<style>
  :root {
    --page: #eef0ed;
    --label: #ffffff;
    --ink: #1d1d1d;
    --ink-soft: #6f6f6f;
    --green-top: #9ccc76;
    --green-mid: #6fb03f;
    --green-deep: #4c9317;
    --on-green: #f4f9ef;
    --badge: #2b3f8c;
  }
  * { box-sizing: border-box; margin: 0; padding: 0; }
  html, body { width: 1200px; height: 1200px; overflow: hidden; }
  body {
    background: var(--page);
    font-family: "Poppins", sans-serif;
    color: var(--ink);
    position: relative;
  }
  .label {
    position: absolute;
    left: 150px; top: 190px;
    width: 900px; height: 820px;
    background: var(--label);
    overflow: hidden;
    box-shadow: 0 2px 14px rgba(0,0,0,0.08);
  }
  .side-panel {
    position: absolute;
    left: 26px; top: 140px;
    width: 540px;
  }
  .section-title {
    font-family: "Barlow Condensed", sans-serif;
    font-weight: 600;
    font-size: 25px;
    line-height: 1.1;
    margin-bottom: 4px;
  }
  .section-text {
    font-size: 23px;
    line-height: 1.38;
    font-weight: 400;
    color: var(--ink);
  }
  .section-text .light { color: var(--ink-soft); font-weight: 300; }
  .section-text .cond { font-family: "Barlow Condensed", sans-serif; font-size: 24px; }
  .usage { margin-bottom: 28px; }
  .warning-box {
    border: 3px solid var(--ink);
    border-radius: 20px;
    padding: 20px 10px 22px 10px;
    width: 500px;
    margin-bottom: 24px;
  }
  .maker {
    position: absolute;
    left: 26px; top: 690px;
    display: flex; align-items: center; gap: 26px;
  }
  .maker-text {
    font-family: "Barlow Condensed", sans-serif;
    font-weight: 700;
    font-size: 22px;
    letter-spacing: 0.2px;
  }
  .made-badge {
    width: 68px; height: 68px;
    border-radius: 50%;
    background: var(--badge);
    border: 4px solid #c83a3a;
  }
  .front-panel {
    position: absolute;
    left: 636px; top: 302px;
    width: 420px; height: 540px;
    background: linear-gradient(160deg, var(--green-mid) 0%, var(--green-top) 35%, var(--green-mid) 65%, var(--green-deep) 100%);
  }
  .product-name {
    position: absolute;
    left: 205px; top: 40px;
    font-family: "Oswald", sans-serif;
    font-weight: 700;
    font-size: 150px;
    line-height: 1;
    color: #ffffff;
    white-space: nowrap;
  }
  .product-sub {
    position: absolute;
    left: 258px; top: 200px;
    font-family: "Oswald", sans-serif;
    font-weight: 300;
    font-size: 60px;
    line-height: 1;
    color: #ffffff;
    white-space: nowrap;
  }
  .benefits {
    position: absolute;
    left: 100px; top: 430px;
    border-left: 2px solid var(--on-green);
    padding-left: 14px;
    font-family: "Barlow Condensed", sans-serif;
    font-size: 19px;
    line-height: 1.45;
    color: var(--on-green);
    white-space: nowrap;
  }
  .benefits strong { font-weight: 700; }
</style>
</head>
<body>
  <div class="label">
    <div class="side-panel">
      <div class="usage">
        <h2 class="section-title">Suggested Use:</h2>
        <p class="section-text"><span class="cond">Take with</span> <span class="light">water 25 minutes before</span> a high-carb<br><span class="cond">or high-fat</span> <span class="light">meal.</span><br><span class="cond">Refer to</span> <span class="light">dosage chart: Fat(g) ÷ 6 =</span> Number of<br><span class="cond">capsules</span></p>
      </div>
      <div class="warning-box">
        <h2 class="section-title">Warning:</h2>
        <p class="section-text"><span class="cond">For adults only.</span> <span class="light">Consult a healthcare</span> provider<br><span class="cond">if you are</span> <span class="light">pregnant, nursing, on</span> medication,<br><span class="cond">or have a</span> <span class="light">medical condition.</span></p>
      </div>
      <div class="storage">
        <h2 class="section-title">Storage:</h2>
        <p class="section-text"><span class="cond">Store at</span> <span class="light">55–75°F. Protect from</span> moisture and heat.</p>
      </div>
    </div>
    <div class="maker">
      <p class="maker-text">MANUFACTURED IN THE USA BY KEP BRIGHTMEALS</p>
      <div class="made-badge" role="img" aria-label="Made in USA badge"></div>
    </div>
    <div class="front-panel">
      <h1 class="product-name">Velo Slate</h1>
      <p class="product-sub">Capsules</p>
      <div class="benefits">
        <p>Advanced Fat + Carb Inhibitor</p>
        <p>Block up to 10g of Fat &amp; 85% of Carbs</p>
        <p>Burn more stored body fat naturally</p>
        <p><strong>60 CAPSULE</strong> - Dietary Supplement</p>
      </div>
    </div>
  </div>
</body>
</html>
```